Corvimo Business Card

Corvimo is a young and energetic software development consultancy. We spend our time on the road working with clients on their sites an meeting new potential customers and employees!

We need a sharp, vibrant and memorable business card that will inspires those that receive it to look after it as it oozes quality and is a nice thing in its own right.

We like bold colours and distinctive design. So show us what you can do.

In terms of information on the card, it would be good to see:

* Our logo (Obviously :) )
* Employee name
* Email
* Website address
* Mobile number
* Full company name (Corvimo ltd)
* Registered company number
* Registered company address

Industry/Entity Type

Software

Requirements
Nice to have
• We are thinking that having a QR Code on the business card could be a good way of adding active marketing. It would be good to see if you are able to merge the kind of element in to your designs!

Maybe something special could be achieved using a visual QR Code like those produced at http://www.pixoranta.example/ ? You have our media so feel free to have a play.

```html
<!DOCTYPE html>
<html lang="en">
<head>
<meta charset="utf-8">
<title>Corvimo Business Card</title>
<link rel="stylesheet" href="https://fonts.googleapis.com/css2?family=Questrial&display=swap">
<style>
  :root {
    --brand-red: #c41e2e;
    --brand-red-dark: #a8161f;
    --ink-grey: #7d7d7d;
    --rule-grey: #bdbdbd;
    --band-grey: #c9c9c9;
    --paper: #ffffff;
    --backdrop: #3a3a3a;
  }
  * { box-sizing: border-box; margin: 0; padding: 0; }
  html, body { width: 1200px; height: 799px; overflow: hidden; }
  body {
    background: var(--backdrop);
    font-family: "Questrial", "Century Gothic", sans-serif;
    position: relative;
  }
  .card {
    position: absolute;
    top: 257px;
    width: 500px;
    height: 286px;
    overflow: hidden;
    box-shadow: 0 10px 30px rgba(0,0,0,.45);
  }
  .card--front { left: 70px; background: var(--paper); }
  .card--back  { left: 630px; background: var(--brand-red); }

  .wordmark {
    position: absolute;
    letter-spacing: 1px;
    line-height: 1;
  }
  .card--front .wordmark {
    left: 34px; top: 34px;
    font-size: 44px;
    color: var(--brand-red);
  }
  .card--back .wordmark {
    left: 0; right: 0; top: 108px;
    text-align: center;
    font-size: 48px;
    color: var(--paper);
  }
  .card--back .back-web {
    position: absolute;
    left: 0; right: 0; top: 170px;
    text-align: center;
    font-size: 13px;
    color: var(--paper);
    letter-spacing: .5px;
  }

  .divider {
    position: absolute;
    left: 34px; right: 34px; top: 116px;
    height: 1px;
    background: var(--rule-grey);
  }
  .contact-list {
    position: absolute;
    left: 34px; top: 128px;
    list-style: none;
    font-size: 12.5px;
    color: var(--ink-grey);
  }
  .contact-list li {
    display: flex;
    align-items: center;
    gap: 9px;
    height: 19px;
  }
  .contact-icon { width: 12px; height: 12px; flex: none; }

  .person {
    position: absolute;
    right: 34px; top: 140px;
    text-align: right;
  }
  .person-name { font-size: 14px; color: var(--brand-red); font-weight: 700; }
  .person-role { font-size: 12px; color: var(--ink-grey); }
  .person-rule {
    position: absolute;
    right: 34px; top: 178px;
    width: 130px; height: 1px;
    background: var(--rule-grey);
  }
  .address {
    position: absolute;
    right: 34px; top: 186px;
    text-align: right;
    font-size: 12.5px;
    line-height: 18px;
    color: var(--ink-grey);
    font-style: normal;
  }
  .footer-band {
    position: absolute;
    left: 0; bottom: 0;
    width: 100%; height: 26px;
  }
</style>
</head>
<body>

<section class="card card--front" aria-label="Card front">
  <div class="wordmark">Corvimo</div>
  <div class="divider"></div>

  <ul class="contact-list">
    <li>
      <svg class="contact-icon" viewBox="0 0 12 12"><circle cx="6" cy="6" r="6" fill="var(--brand-red)"/><path d="M4 3.2 5.2 4.4 4.6 5.2a4 4 0 0 0 2.2 2.2l.8-.6 1.2 1.2-.9.9C5.8 8.8 3.2 6.2 3.1 4.1z" fill="#fff"/></svg>
      084 555 0192
    </li>
    <li>
      <svg class="contact-icon" viewBox="0 0 12 12"><circle cx="6" cy="6" r="6" fill="var(--brand-red)"/><rect x="4.2" y="2.6" width="3.6" height="6.8" rx=".6" fill="#fff"/><rect x="4.8" y="3.4" width="2.4" height="4.4" fill="var(--brand-red)"/></svg>
      084 555 0192
    </li>
    <li>
      <svg class="contact-icon" viewBox="0 0 12 12"><circle cx="6" cy="6" r="6" fill="var(--brand-red)"/><rect x="3" y="4" width="6" height="4.2" fill="#fff"/><path d="M3 4 6 6.4 9 4" fill="none" stroke="var(--brand-red)" stroke-width=".7"/></svg>
      mara@corvimo.com.au
    </li>
    <li>
      <svg class="contact-icon" viewBox="0 0 12 12"><circle cx="6" cy="6" r="6" fill="var(--brand-red)"/><circle cx="6" cy="6" r="3.2" fill="none" stroke="#fff" stroke-width=".8"/><path d="M2.8 6h6.4M6 2.8c-1.6 2-1.6 4.4 0 6.4M6 2.8c1.6 2 1.6 4.4 0 6.4" fill="none" stroke="#fff" stroke-width=".6"/></svg>
      www.corvimo.com.au
    </li>
  </ul>

  <div class="person">
    <div class="person-name">Mara Velden</div>
    <div class="person-role">Director</div>
  </div>
  <div class="person-rule"></div>
  <address class="address">
    2140 N Harlow Road<br>
    Suite 312<br>
    Fairview, Maryland 5410
  </address>

  <svg class="footer-band" viewBox="0 0 500 26" preserveAspectRatio="none" aria-hidden="true">
    <polygon points="0,0 310,0 330,26 0,26" fill="var(--brand-red)"/>
    <polygon points="310,0 500,0 500,26 330,26" fill="var(--band-grey)"/>
  </svg>
</section>

<section class="card card--back" aria-label="Card back">
  <div class="wordmark">Corvimo</div>
  <div class="back-web">www.corvimo.com.au</div>
</section>

</body>
</html>
```